The Harborline Flyer (not postcard)

The Harborline is my financial planning practice. I offer planning and wealth management services to clients.

I want a full 8.5x11 double sided flyer outlining my services - something I can hand out to propsects in person. It is a simple word document that you can see under my account called The Harborline Flyer. I just need it to look very professional and colorful. My logo colors are nice and you can see other things I have made to give you an idea. The only reason I labeled this project is a postcard is that was the only option through Quillmark (how I found you).

I like the phone - fee free to call my cell at 503 417 9862. the winner will be someone who works with me so its as great as it can be.
Updates

Just to be clear I want a full 8.5x11 double sided flyer - any problems email me at martin@corvellagroup.example

thx 

Hi everyone,

No more designs are needed. I have what I need. Thanks 

Target Market(s)

prospects - people with wealth

Industry/Entity Type

Financial

Font styles to use
Serif

Colors
3276b5
f68e4e

Requirements
Must have
• I am going for simplicity with the flyer. If you want less words, I can edit the word doc down further. The text needs to be neatly organized so it is easy to follow. Please match my logo colors.

Nice to have
• financial services - i have 3 sections there. that should all be aligned horizontally next to one another so as to take up less space.

wealth management is its own little world so i would like the company info, financial planning, and wealth management grouped in 3 different sections.

```html
<!DOCTYPE html>
<html lang="en">
<head>
<meta charset="utf-8">
<title>The Harborline Flyer</title>
<link href="https://fonts.googleapis.com/css2?family=Playfair+Display:wght@400;700&family=Open+Sans:wght@400;600;700&family=Great+Vibes&display=swap" rel="stylesheet">
<style>
  :root {
    --brand-blue: #3276b5;
    --sky-blue: #4fa3da;
    --pale-blue: #d3e8f6;
    --brand-orange: #f68e4e;
    --ink: #2b3540;
    --paper: #ffffff;
    --backdrop: #e8edef;
  }
  * { box-sizing: border-box; margin: 0; padding: 0; }
  html, body { width: 1200px; height: 960px; overflow: hidden; }
  body {
    background: var(--backdrop);
    font-family: "Open Sans", Arial, sans-serif;
    color: var(--ink);
  }
  .flyer {
    position: absolute; left: 244px; top: 20px;
    width: 712px; height: 920px;
    background: var(--paper);
    overflow: hidden;
    box-shadow: 0 4px 18px rgba(0,0,0,0.12);
  }
  .flyer-shapes { position: absolute; inset: 0; }
  .hero-photo { position: absolute; left: 392px; top: 96px; }

  .brand {
    position: absolute; right: 26px; top: 30px;
    display: flex; align-items: center; gap: 10px;
  }
  .brand-mark { width: 22px; height: 22px; background: var(--brand-blue); }
  .brand-name {
    font-family: "Playfair Display", Georgia, serif;
    font-weight: 700; font-size: 28px; color: var(--brand-blue);
  }
  .brand-tagline {
    position: absolute; right: 26px; top: 72px;
    font-size: 9px; color: var(--brand-orange); letter-spacing: 0.5px;
  }

  .headline {
    position: absolute; left: 28px; top: 58px; width: 350px;
    font-family: "Playfair Display", Georgia, serif;
    text-transform: uppercase; line-height: 1;
  }
  .headline-lead { font-size: 13px; color: var(--brand-orange); letter-spacing: 1px; }
  .headline-advice { font-size: 33px; color: var(--brand-orange); margin-top: 4px; line-height: 1.02; }
  .headline-amp {
    position: absolute; left: 312px; top: 44px;
    font-family: "Great Vibes", cursive; font-size: 72px; line-height: 1;
    color: var(--brand-orange); text-transform: none;
  }
  .headline-asset { font-size: 94px; color: var(--brand-blue); margin-top: 16px; }
  .headline-management { font-size: 42px; color: var(--brand-blue); margin-top: 2px; }
  .headline-clients { font-size: 25px; color: var(--sky-blue); margin-top: 8px; }

  .about-column {
    position: absolute; left: 24px; top: 462px; width: 240px;
    color: var(--paper);
  }
  .section-title {
    font-family: "Playfair Display", Georgia, serif;
    font-size: 20px; text-transform: uppercase; letter-spacing: 0.5px;
  }
  .about-column .section-title { border-bottom: 1px solid rgba(255,255,255,0.7); padding-bottom: 6px; margin-bottom: 10px; }
  .tick-list { list-style: none; }
  .tick-list li {
    position: relative; padding-left: 18px;
    font-size: 11px; line-height: 1.45; margin-bottom: 8px;
  }
  .tick-list li svg { position: absolute; left: 0; top: 3px; }
  .why-title { margin-top: 18px; }

  .service-options { position: absolute; left: 296px; top: 536px; width: 172px; }
  .service-options .section-title { color: var(--brand-blue); line-height: 1.05; margin-bottom: 12px; }
  .option-card { background: var(--pale-blue); margin-bottom: 10px; padding: 8px 10px 10px; border-top: 3px solid var(--brand-blue); }
  .option-name { font-size: 12px; font-weight: 700; color: var(--brand-blue); line-height: 1.25; }
  .option-text { font-size: 10px; line-height: 1.4; margin-top: 4px; }

  .financial-services { position: absolute; left: 486px; top: 536px; width: 200px; }
  .financial-services .section-title { color: var(--brand-orange); line-height: 1.05; margin-bottom: 8px; }
  .services-intro { font-size: 10px; line-height: 1.4; margin-bottom: 10px; }
  .services-group { font-size: 11px; font-weight: 700; color: var(--brand-orange); margin-bottom: 8px; }
  .service-list { list-style: none; }
  .service-list li {
    background: var(--brand-orange); color: var(--paper);
    font-size: 12px; padding: 6px 12px; margin-bottom: 7px;
  }
</style>
</head>
<body>
<main class="flyer">
  <svg class="flyer-shapes" width="712" height="920" viewBox="0 0 712 920" aria-hidden="true">
    <path d="M0 404 C 200 470 470 470 712 360 L712 400 C 470 516 200 512 0 446 Z" fill="var(--sky-blue)"/>
    <path d="M0 446 C 120 482 220 500 280 506 L280 920 L0 920 Z" fill="var(--brand-blue)"/>
    <rect x="0" y="912" width="712" height="8" fill="var(--brand-blue)"/>
  </svg>

  <svg class="hero-photo" width="320" height="420" viewBox="0 0 320 420" role="img" aria-label="Photo of a smiling retired couple embracing outdoors">
    <defs>
      <linearGradient id="photoTone" x1="0" y1="0" x2="1" y2="1">
        <stop offset="0" stop-color="#f3efe6"/>
        <stop offset="0.55" stop-color="#c9b29a"/>
        <stop offset="1" stop-color="#6f9bc8"/>
      </linearGradient>
    </defs>
    <path d="M0 0 H320 V266 C 200 330 90 350 0 356 Z" fill="url(#photoTone)"/>
  </svg>

  <div class="brand">
    <span class="brand-mark"></span>
    <span class="brand-name">The Harborline</span>
  </div>
  <p class="brand-tagline">Financial Planning &amp; Wealth Management</p>

  <h1 class="headline">
    <div class="headline-lead">Provides</div>
    <div class="headline-advice">Comprehensive<br>Financial Advice</div>
    <div class="headline-asset">Asset</div>
    <div class="headline-management">Management</div>
    <div class="headline-clients">For over 200 clients</div>
    <span class="headline-amp">&amp;</span>
  </h1>

  <section class="about-column">
    <h2 class="section-title">About Us</h2>
    <ul class="tick-list">
      <li><svg width="11" height="9" viewBox="0 0 11 9"><path d="M1 4.5 L4 7.5 L10 1" stroke="#fff" stroke-width="2" fill="none"/></svg>The Harborline is the practice of Martin Ashby, CFP, LLC.</li>
      <li><svg width="11" height="9" viewBox="0 0 11 9"><path d="M1 4.5 L4 7.5 L10 1" stroke="#fff" stroke-width="2" fill="none"/></svg>The Harborline provides comprehensive financial advice and asset management for over 200 clients.</li>
      <li><svg width="11" height="9" viewBox="0 0 11 9"><path d="M1 4.5 L4 7.5 L10 1" stroke="#fff" stroke-width="2" fill="none"/></svg>We have the privilege of managing over $80 million for those households.</li>
      <li><svg width="11" height="9" viewBox="0 0 11 9"><path d="M1 4.5 L4 7.5 L10 1" stroke="#fff" stroke-width="2" fill="none"/></svg>Martin is a 15-year financial planning veteran who graduated from Ridgefield University with a degree in finance and has worked with families ever since.</li>
    </ul>
    <h2 class="section-title why-title">Why Plan With Us</h2>
    <ul class="tick-list">
      <li><svg width="11" height="9" viewBox="0 0 11 9"><path d="M1 4.5 L4 7.5 L10 1" stroke="#fff" stroke-width="2" fill="none"/></svg>Clear advice.</li>
      <li><svg width="11" height="9" viewBox="0 0 11 9"><path d="M1 4.5 L4 7.5 L10 1" stroke="#fff" stroke-width="2" fill="none"/></svg>Strong personal focus to help clients protect and grow wealth through balanced investments.</li>
      <li><svg width="11" height="9" viewBox="0 0 11 9"><path d="M1 4.5 L4 7.5 L10 1" stroke="#fff" stroke-width="2" fill="none"/></svg>Reduce your tax liability.</li>
      <li><svg width="11" height="9" viewBox="0 0 11 9"><path d="M1 4.5 L4 7.5 L10 1" stroke="#fff" stroke-width="2" fill="none"/></svg>Efficiently have assets in order.</li>
    </ul>
  </section>

  <section class="service-options">
    <h2 class="section-title">Client Service<br>Options</h2>
    <div class="option-card">
      <div class="option-name">Asset Management</div>
      <p class="option-text">We charge a flat 1% fee to provide wealth management.</p>
    </div>
    <div class="option-card">
      <div class="option-name">Financial Planning &amp; Advice</div>
      <p class="option-text">We create a plan with comprehensive financial and education planning advice.</p>
    </div>
    <div class="option-card">
      <div class="option-name">Portfolio Asset Management</div>
      <p class="option-text">Platforms use our portfolio models.</p>
    </div>
  </section>

  <section class="financial-services">
    <h2 class="section-title">Financial<br>Services</h2>
    <p class="services-intro">We advise clients on all of the following areas to build your custom financial plan.</p>
    <div class="services-group">Personal Finance &amp; Life Events</div>
    <ul class="service-list">
      <li>cash management</li>
      <li>cash flow management</li>
      <li>retirement planning</li>
      <li>education planning</li>
      <li>home purchase</li>
      <li>liability management</li>
    </ul>
  </section>
</main>
</body>
</html>
```